Grand Volley Pickleball Tournament

Design a poster for the Tidewater Rally Series, a pickleball tournament series. Each event will have it's own poster with a different design. The posters should be different but related graphically. The first assignment is Posters 1 and 2. The posters should be bold, exciting, fun and show movement. The attached files are for content, hierarchy for text but not design. Logo typeface: Legend 54. Logo blue: cmyk blue: 2b3990 R: 43 G:57 B:144
Please contact me with questions.

```html
<!DOCTYPE html>
<html lang="en">
<head>
<meta charset="utf-8">
<title>Tidewater Rally Series – Grand Volley Pickleball Tournament</title>
<link href="https://fonts.googleapis.com/css2?family=Teko:wght@600&family=League+Spartan:wght@700&family=Questrial&family=Signika:wght@700&display=swap" rel="stylesheet">
<style>
  :root {
    --navy: #2b2766;
    --brand-blue: #2b3990;
    --deep-blue: #1b1486;
    --yellow: #f7e635;
    --white: #ffffff;
    --title-white: #ececec;
    --field-green: #7a9477;
    --field-light: #9fbc96;
    --ink: #111111;
  }
  html, body { margin: 0; padding: 0; overflow: hidden; }
  body { width: 849px; height: 1200px; background: var(--white); }
  .poster {
    position: relative; width: 849px; height: 1200px; overflow: hidden;
    background: var(--field-green);
  }
  .backdrop { position: absolute; inset: 0; }
  .paddle-art {
    position: absolute; left: 0; top: 490px; width: 420px; height: 560px;
    background: radial-gradient(ellipse at 45% 40%, rgba(210,214,214,.9), rgba(120,130,135,.55) 60%, rgba(80,90,95,0) 80%);
  }
  .series-title {
    position: absolute; left: 0; width: 849px; top: 196px; margin: 0; text-align: center;
    font-family: "Teko", sans-serif; font-weight: 600; line-height: 1; color: var(--title-white);
  }
  .series-title .name { display: block; font-size: 92px; letter-spacing: 1px; }
  .series-title .tag { display: block; margin-top: -8px; font-size: 54px; letter-spacing: 3px; }
  .sanction-badge {
    position: absolute; left: 40px; top: 344px; width: 166px; height: 130px;
    border-radius: 10px; background: var(--brand-blue);
  }
  .headline {
    position: absolute; right: 36px; top: 478px; margin: 0; text-align: right;
    font-family: "Signika", sans-serif; font-weight: 700; font-size: 30.5px; line-height: 34px;
    color: var(--yellow); letter-spacing: .5px;
  }
  .info-panel {
    position: absolute; left: 18px; top: 568px; width: 812px; height: 612px;
    border-radius: 14px; background: rgba(232,238,228,.72); text-align: center;
  }
  .info-panel .light-band { position: absolute; left: 0; right: 0; top: 406px; height: 132px; background: rgba(255,255,255,.78); }
  .events { position: relative; padding-top: 38px; }
  .event { margin-bottom: 22px; }
  .event:last-child { margin-bottom: 0; }
  .event-name { font-family: "League Spartan", sans-serif; font-weight: 700; font-size: 31px; line-height: 28px; color: var(--ink); }
  .event-date { font-family: "Questrial", sans-serif; font-size: 23px; line-height: 26px; color: var(--ink); }
  .divisions { position: relative; margin-top: 16px; font-family: "League Spartan", sans-serif; font-weight: 700; }
  .divisions .main { font-size: 38px; line-height: 34px; color: var(--deep-blue); }
  .divisions .sub { font-size: 27px; line-height: 26px; color: var(--ink); }
  .contact { position: relative; margin-top: 28px; font-family: "Questrial", sans-serif; font-size: 19.5px; line-height: 25.5px; color: #222; }
  .contact .lead { font-family: "League Spartan", sans-serif; font-weight: 700; font-size: 19px; color: var(--ink); }
</style>
</head>
<body>
<main class="poster">
  <svg class="backdrop" width="849" height="1200" viewBox="0 0 849 1200" aria-hidden="true">
    <path d="M0 285 Q420 420 849 300 L849 0 L0 0 Z" fill="var(--navy)"/>
    <path d="M0 285 Q430 430 849 300 L849 330 Q640 460 0 495 Z" fill="var(--white)"/>
    <path d="M0 495 Q420 470 582 436 Q520 470 0 525 Z" fill="var(--white)"/>
    <rect x="0" y="1106" width="849" height="94" fill="var(--field-light)"/>
  </svg>
  <div class="paddle-art" role="img" aria-label="Illustration of a pickleball paddle striking a ball"></div>
  <h1 class="series-title"><span class="name">TIDEWATER</span><span class="tag">RALLY SERIES</span></h1>
  <div class="sanction-badge" role="img" aria-label="Sanctioning body badge"></div>
  <p class="headline">NPA SANCTIONED<br>PICKLEBALL TOURNAMENT</p>
  <section class="info-panel">
    <div class="light-band"></div>
    <div class="events">
      <div class="event"><div class="event-name">GRAND VOLLEY</div><div class="event-date">November 23-24, 2019</div></div>
      <div class="event"><div class="event-name">HARBORVIEW OPEN</div><div class="event-date">February 15-16, 2020</div></div>
      <div class="event"><div class="event-name">BAYFRONT SMASH</div><div class="event-date">September 12-13, 2020</div></div>
      <div class="event"><div class="event-name">FINAL RALLY</div><div class="event-date">November 21-22, 2020</div></div>
    </div>
    <div class="divisions">
      <div class="main">WOMEN’S, MEN’S AND MIXED DOUBLES</div>
      <div class="sub">BRIGHTLINE FLUX YELLOW INDOOR BALL</div>
      <div class="sub">CASH PRIZES!</div>
    </div>
    <div class="contact">
      <div class="lead">Sponsorship Opportunities Available</div>
      <div>Questions: tidewaterrallyseries@example.com</div>
      <div>Registration: http://rallybrackets.example.com/</div>
      <div>Harborview Sportsplex, 120 Shoreline Ave, Bayport, MA</div>
      <div>Venue of the 2019 NPA Atlantic Regional</div>
    </div>
  </section>
</main>
</body>
</html>
```